HOT TUB - SPAS service needs an business card

I need an business for my company who his specialise in a maintenance,water treatment and cleaning of Hot Tub - Spas for commercial and residential customers. The company operate mainly in the ski resort of Chamonix, Megève and St Gervais. The final product should communicate pure water, cleanest and professional for luxury property's.
I have upload a logo but any improvement on it is welcome.(color,size, details etc..) or any other idea. Thank you
Company Name: 58 BAINS
My name: Laurent Mazeyrac
Email: lmazey@courrielo.fr
Tel: +33 (0)6 81 52 29 07
Description to be on the card in french(first langage) and in English:
- Spas service
- Entretien, traitement eau, nettoyage.
- Maintenance, water treatment, cleaning.

```html
<!DOCTYPE html>
<html lang="fr">
<head>
<meta charset="utf-8">
<title>58 BAINS – cartes de visite</title>
<link href="https://fonts.googleapis.com/css2?family=Didact+Gothic&display=swap" rel="stylesheet">
<style>
  :root {
    --page: #eef1f4;
    --blue-light: #6aaeea;
    --blue-deep: #3f86d4;
    --white: #ffffff;
    --band-tint: #f3f6f9;
    --ink: #4a4f57;
    --ink-dark: #2b4d74;
    --rule: #4a8fd8;
  }
  * { box-sizing: border-box; margin: 0; padding: 0; }
  html, body { width: 1200px; height: 800px; overflow: hidden; }
  body {
    background: var(--page);
    font-family: "Didact Gothic", "Helvetica Neue", sans-serif;
    display: flex; flex-direction: column; align-items: center; justify-content: center;
    gap: 30px;
  }
  .card {
    position: relative; width: 620px; height: 354px; overflow: hidden;
    background: linear-gradient(160deg, var(--blue-light) 0%, var(--blue-deep) 100%);
    box-shadow: 0 6px 18px rgba(30, 60, 100, .18);
    color: var(--white);
  }
  .brand { position: absolute; display: flex; align-items: center; gap: 18px; }
  .brand-mark { width: 60px; height: 60px; border: 2px solid var(--white); }
  .brand-name { font-size: 56px; letter-spacing: 1px; line-height: 1; color: var(--white); }

  .front .brand { left: 34px; top: 26px; }
  .rule { position: absolute; left: 0; right: 0; background: var(--white); }
  .front .rule-top { top: 104px; height: 4px; }
  .front .rule-bottom { top: 306px; height: 4px; }
  .services { position: absolute; left: 112px; top: 116px; color: var(--ink-dark); font-size: 14px; line-height: 1.3; letter-spacing: .5px; }
  .contact-band { position: absolute; left: 0; right: 0; top: 186px; height: 108px; background: var(--white); }
  .contact-line {
    display: flex; align-items: center; gap: 12px; height: 36px; padding-left: 80px;
    color: var(--ink); font-size: 15px; letter-spacing: 2.5px;
    border-bottom: 1px solid var(--rule);
  }
  .contact-line:last-child { border-bottom: none; }
  .contact-icon { width: 16px; height: 16px; fill: var(--ink); }

  .back .brand { left: 190px; top: 70px; }
  .back .rule-top { top: 190px; height: 6px; }
  .back .pattern-band {
    position: absolute; left: 0; right: 0; top: 206px; height: 80px;
    background: linear-gradient(90deg, var(--band-tint), var(--white));
  }
</style>
</head>
<body>

  <section class="card front" aria-label="Recto de la carte">
    <div class="brand">
      <span class="brand-mark"></span>
      <span class="brand-name">58 BAINS</span>
    </div>
    <div class="rule rule-top"></div>
    <div class="services">
      <p>spas service</p>
      <p>- entretien, traitement eau, nettoyage</p>
      <p>- maintenance, water treatment, cleaning</p>
    </div>
    <div class="contact-band">
      <div class="contact-line">
        <svg class="contact-icon" viewBox="0 0 16 16" aria-hidden="true"><circle cx="8" cy="5" r="3.5"/><path d="M1.5 16c0-4 3-6 6.5-6s6.5 2 6.5 6z"/></svg>
        <span>Laurent Mazeyrac</span>
      </div>
      <div class="contact-line">
        <svg class="contact-icon" viewBox="0 0 16 16" aria-hidden="true"><path d="M1 3h14v10H1z" fill="none" stroke="#4a4f57" stroke-width="1.4"/><path d="M1 3l7 6 7-6" fill="none" stroke="#4a4f57" stroke-width="1.4"/></svg>
        <span>email: lmazey@courrielo.fr</span>
      </div>
      <div class="contact-line">
        <svg class="contact-icon" viewBox="0 0 16 16" aria-hidden="true"><path d="M4 1l3 3-2 2c1 2 3 4 5 5l2-2 3 3-2 3C7 15 1 9 1 3z"/></svg>
        <span>tel.: +33 (0)6 81 52 29 07</span>
      </div>
    </div>
    <div class="rule rule-bottom"></div>
  </section>

  <section class="card back" aria-label="Verso de la carte">
    <div class="brand">
      <span class="brand-mark"></span>
      <span class="brand-name">58 BAINS</span>
    </div>
    <div class="rule rule-top"></div>
    <div class="pattern-band" role="img" aria-label="Bande blanche à motif hexagonal discret"></div>
  </section>

</body>
</html>
```